brindlewood carpentry business card 2.0

id like to get some extra info added to my current business card ,but i am also open to a new design as well ,id like it to be a clean professional look
i have attached the original card files, i have also attached the ridgemark guild logo and licensed builder logo that id like to add to all the current info on the old card
also the color green is important as seen in the company logo

Industry/Entity Type

Carpentry

Colors
9bcb3c

```html
<!DOCTYPE html>
<html lang="en">
<head>
<meta charset="utf-8">
<title>Brindlewood Carpentry – Business Card</title>
<link href="https://fonts.googleapis.com/css2?family=Montserrat:wght@400;500;600;700&display=swap" rel="stylesheet">
<style>
  :root {
    --bg: #e8e8e8;
    --charcoal: #2b2b2b;
    --paper: #f7f7f5;
    --green: #9bcb3c;
    --white: #ffffff;
    --ink: #1c1c1c;
    --badge-blue: #1f4f9a;
  }
  * { box-sizing: border-box; margin: 0; padding: 0; }
  html, body { width: 1200px; height: 794px; overflow: hidden; }
  body {
    background: var(--bg);
    font-family: "Montserrat", sans-serif;
    position: relative;
  }
  .card {
    position: absolute;
    top: 242px;
    width: 540px;
    height: 309px;
    box-shadow: 0 4px 14px rgba(0,0,0,0.18);
    overflow: hidden;
  }
  .card--front { left: 40px; background: var(--charcoal); display: flex; align-items: center; justify-content: center; }
  .card--back { left: 620px; display: flex; }

  .wordmark { display: flex; align-items: center; gap: 12px; font-weight: 500; letter-spacing: 0.04em; text-transform: uppercase; }
  .wordmark__square { width: 10px; height: 10px; background: currentColor; flex: none; }
  .wordmark__text { display: flex; flex-direction: column; line-height: 1.05; }
  .wordmark--front { color: var(--white); }
  .wordmark--front .wordmark__name { font-size: 40px; }
  .wordmark--front .wordmark__trade { font-size: 20px; letter-spacing: 0.12em; }
  .wordmark--back { color: var(--ink); }
  .wordmark--back .wordmark__name { font-size: 21px; }
  .wordmark--back .wordmark__trade { font-size: 11px; letter-spacing: 0.12em; }
  .wordmark--back .wordmark__square { width: 7px; height: 7px; }

  .back__brand {
    width: 42%;
    background: var(--paper);
    position: relative;
    padding: 96px 0 0 22px;
  }
  .back__badges { position: absolute; left: 40px; bottom: 30px; display: flex; gap: 22px; align-items: center; }
  .badge--guild { width: 38px; height: 46px; background: var(--badge-blue); }
  .badge--licence { width: 50px; height: 50px; border-radius: 50%; background: var(--green); opacity: 0.85; }

  .back__details {
    flex: 1;
    background: var(--charcoal);
    color: var(--white);
    position: relative;
    padding: 66px 20px 0 34px;
  }
  .back__accent { position: absolute; left: 0; top: 60px; width: 5px; height: 170px; background: var(--green); }
  .person__name { font-size: 20px; font-weight: 600; }
  .person__role { font-size: 12px; font-weight: 400; margin-top: 4px; }
  .contact { list-style: none; margin-top: 48px; display: flex; flex-direction: column; gap: 9px; }
  .contact__item { display: flex; align-items: center; gap: 12px; font-size: 12px; font-weight: 500; }
  .contact__item svg { width: 15px; height: 15px; flex: none; }
  .contact__strong { font-weight: 700; }
</style>
</head>
<body>
  <section class="card card--front">
    <div class="wordmark wordmark--front">
      <span class="wordmark__square"></span>
      <span class="wordmark__text">
        <span class="wordmark__name">Brindlewood</span>
        <span class="wordmark__trade">Carpentry</span>
      </span>
    </div>
  </section>

  <section class="card card--back">
    <div class="back__brand">
      <div class="wordmark wordmark--back">
        <span class="wordmark__square"></span>
        <span class="wordmark__text">
          <span class="wordmark__name">Brindlewood</span>
          <span class="wordmark__trade">Carpentry</span>
        </span>
      </div>
      <div class="back__badges">
        <div class="badge badge--guild" role="img" aria-label="Ridgemark Guild membership badge"></div>
        <div class="badge badge--licence" role="img" aria-label="Licensed building practitioner badge"></div>
      </div>
    </div>
    <div class="back__details">
      <span class="back__accent"></span>
      <p class="person__name">Marcus Hale</p>
      <p class="person__role">Director Brindlewood Carpentry Ltd</p>
      <ul class="contact">
        <li class="contact__item">
          <svg viewBox="0 0 16 16" fill="none" stroke="#9bcb3c" stroke-width="1.4" stroke-linejoin="round"><path d="M4 2l2.5 3-1.5 1.5c.8 1.8 2.2 3.2 4 4L10.5 9l3 2.5-1.5 2.3C7 13.5 2.5 9 2.2 3.5z"/></svg>
          02104419386
        </li>
        <li class="contact__item">
          <svg viewBox="0 0 16 16" fill="none" stroke="#9bcb3c" stroke-width="1.4" stroke-linejoin="round"><rect x="1.5" y="3.5" width="13" height="9"/><path d="M1.5 3.5l6.5 5 6.5-5"/></svg>
          marcus@brindlewoodcarpentry.co.nz
        </li>
        <li class="contact__item">
          <svg viewBox="0 0 16 16" fill="none" stroke="#9bcb3c" stroke-width="1.3"><circle cx="8" cy="8" r="6.3"/><ellipse cx="8" cy="8" rx="2.8" ry="6.3"/><path d="M1.7 8h12.6M2.8 4.8h10.4M2.8 11.2h10.4"/></svg>
          <span>www.<span class="contact__strong">brindlewoodcarpentry</span>.co.nz</span>
        </li>
      </ul>
    </div>
  </section>
</body>
</html>
```